Logo and bag for Turkish coffee brand

We are a coffee roasting company. We need a logo for our new Turkish coffee brand. We are targeting C+ to A- customer segment. Our brand is above average in pricing and can be expressed as very good in quality or a bit less than excellentOur brand name is قهواكBinnitak is an Arabic word that means "Your coffee" and if read in a different way it means "I love You"

Target Market(s)

We are selling in Egyptian market for customer segments from C+ and up to A-

Logo Text

Binnitak بنّيتك

Requirements
Must have
• 1. The logo must contain brand name in Arabic good to have it in Arabic and English if possible.
• 2. All text content must be in Arabic and good to be in both Arabic and English
• 3. The package must include two spaces for limited text paragraphs
• an area for production date and expiry.
• 4. An area for selecting variants of the product. Our coffee has light-medium-dark roasted (فاتح - وسط - غامق)
• Plain or flavored (سادة - محوج)

```html
<!DOCTYPE html>
<html lang="ar">
<head>
<meta charset="utf-8">
<title>Binnitak – Turkish Coffee Bag</title>
<link href="https://fonts.googleapis.com/css2?family=Amiri:wght@400;700&family=Reem+Kufi:wght@600&display=swap" rel="stylesheet">
<style>
  :root {
    --page-bg: #f4f1ec;
    --paper-light: #f8ecd3;
    --paper-mid: #efd9b0;
    --paper-edge: #e2bf85;
    --side-light: #f3e4c6;
    --side-dark: #e4c893;
    --ochre: #e8a94a;
    --brown: #7a4a22;
    --brown-soft: #a97a4e;
    --gold: #f2cc55;
    --seal-red: #c4161c;
    --label-white: #fffaf0;
  }
  * { margin: 0; padding: 0; box-sizing: border-box; }
  html, body {
    width: 824px; height: 1200px; overflow: hidden;
    background: var(--page-bg);
  }
  .canvas { position: relative; width: 824px; height: 1200px; }

  .bag-front {
    position: absolute; left: 60px; top: 70px;
    width: 520px; height: 1060px;
    background:
      radial-gradient(circle at 30% 20%, rgba(232,169,74,.25), transparent 40%),
      radial-gradient(circle at 80% 70%, rgba(169,122,78,.25), transparent 45%),
      radial-gradient(circle at 20% 85%, rgba(232,169,74,.3), transparent 35%),
      linear-gradient(170deg, var(--paper-light), var(--paper-mid) 60%, var(--paper-edge));
    box-shadow: 0 10px 30px rgba(90,60,30,.18);
  }
  .top-fold {
    position: absolute; left: 0; top: 0; width: 100%; height: 60px;
    border-bottom: 2px solid rgba(169,122,78,.35);
  }
  .brand-badge {
    position: absolute; left: 60px; top: 120px;
    width: 400px; height: 400px;
  }
  .brand-name {
    position: absolute; inset: 0;
    display: flex; flex-direction: column; align-items: center; justify-content: center;
    font-family: 'Amiri', serif; font-weight: 700; color: var(--brown);
    line-height: 1.05;
  }
  .brand-name .latin { font-size: 80px; }
  .brand-name .arabic { font-size: 72px; }
  .seal {
    position: absolute; left: 360px; top: 545px;
    width: 116px; height: 116px; border-radius: 50%;
    background: var(--seal-red);
  }
  .landmark-illustration {
    position: absolute; left: 30px; top: 610px;
    width: 310px; height: 300px;
    background: linear-gradient(180deg, rgba(169,122,78,.05), rgba(169,122,78,.28));
    border-radius: 6px;
  }
  .variant {
    position: absolute; bottom: 80px;
    font-family: 'Amiri', serif; font-weight: 700;
    font-size: 60px; line-height: 1; color: var(--label-white);
    text-shadow: 0 2px 6px rgba(122,74,34,.7);
  }
  .variant.flavour { left: 50px; }
  .variant.roast { right: 60px; }

  .bag-side {
    position: absolute; left: 580px; top: 70px;
    width: 184px; height: 1060px;
    background: linear-gradient(90deg, var(--side-dark), var(--side-light) 40%, var(--side-light));
    box-shadow: 0 10px 30px rgba(90,60,30,.14);
    padding: 90px 16px 40px;
    display: flex; flex-direction: column; align-items: center;
  }
  .stamp-illustration {
    width: 140px; height: 180px; border-radius: 70px;
    background: radial-gradient(circle, rgba(232,169,74,.45), rgba(232,169,74,.15));
    border: 2px solid rgba(232,169,74,.6);
  }
  .product-info {
    margin-top: 40px; width: 100%;
    font-family: 'Amiri', serif; font-size: 13px; line-height: 1.5;
    color: var(--brown);
  }
  .product-info p { margin-bottom: 4px; }
  .product-info b { font-weight: 700; }
  .dates { margin-top: 14px; border-top: 1px solid rgba(122,74,34,.35); padding-top: 8px; }
  .side-brand {
    margin-top: auto; margin-bottom: 60px;
    display: flex; flex-direction: column; align-items: center;
    font-family: 'Amiri', serif; font-weight: 700; color: var(--brown);
    line-height: 1.1;
  }
  .side-brand .latin { font-size: 30px; }
  .side-brand .arabic { font-size: 28px; }
</style>
</head>
<body>
<main class="canvas">
  <section class="bag-front">
    <div class="top-fold"></div>

    <div class="brand-badge">
      <svg width="400" height="400" viewBox="0 0 400 400">
        <circle cx="200" cy="200" r="195" fill="none" stroke="var(--gold)" stroke-width="6" stroke-dasharray="6 5"/>
        <circle cx="200" cy="200" r="186" fill="rgba(248,236,211,.55)"/>
      </svg>
      <div class="brand-name">
        <span class="latin">Binnitak</span>
        <span class="arabic">بنّيتك</span>
      </div>
    </div>

    <div class="seal"></div>

    <div class="landmark-illustration" role="img" aria-label="Sepia line drawing of a domed mosque with minarets"></div>

    <span class="variant flavour">سادة</span>
    <span class="variant roast">وسط</span>
  </section>

  <aside class="bag-side">
    <div class="stamp-illustration" role="img" aria-label="Gold engraved stamp showing a traditional coffee grinder"></div>

    <div class="product-info">
      <p><b>Ingredients:</b> 100% ground Arabica coffee</p>
      <p><b>Type:</b> Medium roast</p>
      <p><b>Grind:</b> Extra fine</p>
      <p><b>Net weight:</b> 100 g</p>
      <div class="dates">
        <p><b>Production date:</b></p>
        <p><b>Expiry date:</b></p>
      </div>
    </div>

    <div class="side-brand">
      <span class="latin">Binnitak</span>
      <span class="arabic">بنّيتك</span>
    </div>
  </aside>
</main>
</body>
</html>
```